Ray Penwick Foundation
Business card and letterhead for a non profit - Miscellaneous
Business card and letterhead for a non profit
Professional
Marla Penwick
P.O. Box 84 Glen Harbor, PA 19217
raypenwickfoundation@mailvista.net
www.raypenwickfoundation.org
Business card: I would like the foundation logo to be the one side. Then information on the other side.

```html
<!DOCTYPE html>
<html lang="en">
<head>
<meta charset="utf-8">
<title>Ray Penwick Foundation — Stationery</title>
<link rel="stylesheet" href="https://fonts.googleapis.com/css2?family=Cinzel:wght@400;600&display=swap">
<style>
  :root {
    --backdrop: #646466;
    --paper: #ffffff;
    --green: #0db14b;
    --blue: #1b8fd0;
    --ink: #3a3a3a;
    --card-dark: #262626;
    --watermark: #e9f6ee;
  }
  * { margin: 0; padding: 0; box-sizing: border-box; }
  html, body { width: 1200px; height: 1200px; overflow: hidden; }
  body { background: var(--backdrop); font-family: "Cinzel", serif; color: var(--ink); position: relative; }

  .letterhead { position: absolute; left: 94px; top: 102px; width: 704px; height: 996px; background: var(--paper); overflow: hidden; }
  .brand { position: absolute; display: flex; align-items: center; gap: 8px; }
  .brand-dot { width: 14px; height: 14px; border-radius: 50%; background: var(--blue); flex: none; }
  .brand-name { color: var(--green); font-weight: 400; line-height: 1.05; letter-spacing: 0.04em; text-transform: uppercase; }
  .letterhead .brand { left: 0; right: 0; top: 150px; justify-content: center; }
  .letterhead .brand-name { font-size: 30px; }
  .letterhead .brand-dot { width: 20px; height: 20px; }

  .watermark { position: absolute; left: 94px; top: 226px; width: 560px; height: 560px; border-radius: 50%; background: var(--watermark); opacity: 0.7; }

  .lh-contact { position: absolute; font-size: 11px; line-height: 15px; letter-spacing: 0.02em; }
  .lh-address { left: 339px; top: 912px; }
  .lh-lines { left: 497px; top: 912px; }
  .lh-email { right: 12px; top: 943px; font-size: 10px; text-transform: uppercase; }
  .label { color: var(--green); font-weight: 600; }

  .wave { position: absolute; left: 0; bottom: 0; width: 100%; }
  .lh-web { position: absolute; left: 25px; bottom: 22px; color: #fff; font-size: 9px; text-transform: uppercase; letter-spacing: 0.03em; }

  .card { position: absolute; left: 809px; width: 298px; height: 170px; border-radius: 16px; overflow: hidden; }
  .card-front { top: 748px; background: var(--paper); }
  .card-back { top: 928px; background: var(--card-dark); display: flex; align-items: center; justify-content: center; }
  .card-front .brand { left: 10px; top: 40px; }
  .card-front .brand-name { font-size: 15px; }
  .card-back .brand { position: static; }
  .card-back .brand-name { font-size: 17px; }

  .card-person { position: absolute; right: 10px; top: 91px; color: var(--green); font-size: 10px; font-weight: 600; letter-spacing: 0.03em; }
  .card-person::after { content: ""; position: absolute; right: -10px; top: -3px; width: 5px; height: 17px; background: var(--blue); }
  .card-address { position: absolute; left: 10px; top: 116px; font-size: 6.5px; line-height: 9px; }
  .card-lines { position: absolute; right: 10px; top: 118px; font-size: 6.5px; line-height: 10px; text-align: right; }
  .card-email { text-transform: uppercase; font-size: 5.6px; }
  .card-web { position: absolute; left: 10px; bottom: 8px; color: #fff; font-size: 5px; text-transform: uppercase; }
</style>
</head>
<body>

<section class="letterhead" aria-label="Letterhead">
  <div class="brand">
    <span class="brand-dot"></span>
    <span class="brand-name">Ray Penwick Foundation</span>
  </div>

  <div class="watermark" role="img" aria-label="Faint background circle in pale green"></div>

  <p class="lh-contact lh-address">P.O. Box 84<br>Glen Harbor, PA 19217</p>
  <p class="lh-contact lh-lines"><span class="label">P</span> : 215-555-0148<br><span class="label">F</span> : 215-555-0193</p>
  <p class="lh-contact lh-email">raypenwickfoundation@mailvista.net</p>

  <svg class="wave" viewBox="0 0 704 56" height="56" preserveAspectRatio="none">
    <path d="M0 10 C150 4 300 14 420 30 C520 44 620 48 704 44 L704 56 L0 56 Z" fill="var(--green)"/>
    <path d="M0 7 C150 1 300 11 420 27 C520 41 620 45 704 41" fill="none" stroke="var(--paper)" stroke-width="3"/>
    <path d="M0 4 C150 -2 300 8 420 24" fill="none" stroke="var(--blue)" stroke-width="4"/>
    <path d="M440 42 C540 50 640 48 704 42" fill="none" stroke="var(--blue)" stroke-width="3"/>
  </svg>
  <p class="lh-web">www.raypenwickfoundation.org</p>
</section>

<section class="card card-front" aria-label="Business card, front">
  <div class="brand">
    <span class="brand-dot"></span>
    <span class="brand-name">Ray Penwick Foundation</span>
  </div>
  <p class="card-person">Marla Penwick</p>
  <p class="card-address">P.O. Box 84<br>Glen Harbor, PA 19217</p>
  <p class="card-lines"><span class="label">P</span> : 215-555-0148<br><span class="label">F</span> : 215-555-0193<br><span class="card-email">raypenwickfoundation@mailvista.net</span></p>
  <svg class="wave" viewBox="0 0 298 30" height="30" preserveAspectRatio="none">
    <path d="M0 8 C60 2 130 6 200 18 C240 25 270 24 298 20 L298 30 L0 30 Z" fill="var(--green)"/>
    <path d="M0 5 C60 -1 130 3 200 15" fill="none" stroke="var(--blue)" stroke-width="2"/>
    <path d="M190 22 C240 28 270 26 298 22" fill="none" stroke="var(--blue)" stroke-width="2"/>
  </svg>
  <p class="card-web">www.raypenwickfoundation.org</p>
</section>

<section class="card card-back" aria-label="Business card, back">
  <div class="brand">
    <span class="brand-dot"></span>
    <span class="brand-name">Ray Penwick Foundation</span>
  </div>
</section>

</body>
</html>
```